BKA

Please send us some options for letterhead I attached our Logo. In addition to the Logo we need this information somewhere on the page

47 Fenbury Lane
Harlow Bay, CT 06417
203-481-7629

```html
<!DOCTYPE html>
<html lang="en">
<head>
<meta charset="utf-8">
<title>BKA Letterhead</title>
<link rel="stylesheet" href="https://fonts.googleapis.com/css2?family=Arimo:wght@400;700&display=swap">
<style>
  :root {
    --paper: #ffffff;
    --brown: #544542;
    --blue-deep: #1f6fc9;
    --blue-light: #5cc2f0;
    --ink: #231f20;
  }
  html, body {
    margin: 0;
    padding: 0;
    overflow: hidden;
    background: var(--paper);
  }
  .letterhead {
    position: relative;
    width: 848px;
    height: 1200px;
    background: var(--paper);
    overflow: hidden;
    font-family: "Arimo", Arial, sans-serif;
    color: var(--ink);
  }
  .header-swoosh {
    position: absolute;
    top: 0;
    left: 0;
    width: 848px;
    height: 120px;
  }
  .brand {
    position: absolute;
    top: 83px;
    left: 594px;
    display: flex;
    align-items: center;
    gap: 14px;
  }
  .brand-mark {
    width: 60px;
    height: 60px;
    background: var(--brown);
  }
  .brand-name {
    font-size: 40px;
    font-weight: 700;
    letter-spacing: 1px;
    color: var(--brown);
    line-height: 1;
  }
  .contact {
    position: absolute;
    top: 172px;
    left: 594px;
    margin: 0;
    font-style: normal;
    font-size: 14.5px;
    line-height: 20px;
    color: var(--ink);
  }
</style>
</head>
<body>
  <main class="letterhead">
    <svg class="header-swoosh" viewBox="0 0 848 120" aria-hidden="true">
      <defs>
        <linearGradient id="swooshBlue" x1="0" y1="0" x2="1" y2="0">
          <stop offset="0" stop-color="var(--blue-deep)"/>
          <stop offset="0.5" stop-color="var(--blue-light)"/>
          <stop offset="1" stop-color="var(--blue-deep)"/>
        </linearGradient>
      </defs>
      <path d="M0 0 H700 Q380 50 0 113 Z" fill="var(--brown)"/>
      <path d="M0 113 Q420 40 848 0 V8 Q440 52 0 115 Z" fill="url(#swooshBlue)"/>
    </svg>

    <div class="brand">
      <span class="brand-mark"></span>
      <span class="brand-name">BKA</span>
    </div>

    <address class="contact">
      47 Fenbury Lane<br>
      Harlow Bay, CT 06417<br>
      203-481-7629
    </address>
  </main>
</body>
</html>
```